Consulting company requires a logo and business card design

I require a logo/business card design for a new company based in Sexsmith Alberta called TanRidge Field Advisory Ltd. I plan to provide the following services: Construction management/inspection for the oil and gas industry, as well as general consulting for Asset Management, fleet management, etc. Have attached a copy of resume for use as guide for

Target Market(s)

Businesses within the oil and gas production, construction and shipping industry

Industry/Entity Type

Oil And Gas

Contact Information for Business Card

Believe should highlight, services offered, safety, quality,

Logo Text

TanRidge Field Advisory (TRFA) ?

Font styles to use
Script

Requirements
Must have
• Open to all options

```html
<!DOCTYPE html>
<html lang="en">
<head>
<meta charset="utf-8">
<title>TanRidge Field Advisory Ltd – Identity</title>
<link rel="stylesheet" href="https://fonts.googleapis.com/css2?family=Cinzel:wght@600&family=Open+Sans:wght@400&display=swap">
<style>
  :root {
    --brand-blue: #1d3f86;
    --brand-grey: #4a4a4a;
    --charcoal: #2b2b2b;
    --charcoal-light: #4d4d4d;
    --stage: #dcdcde;
    --paper: #ffffff;
    --rule: #c9c9c9;
    --text: #2a2a2a;
  }
  * { margin: 0; padding: 0; box-sizing: border-box; }
  html, body { width: 994px; height: 1200px; overflow: hidden; }
  body { position: relative; background: var(--paper); font-family: "Open Sans", sans-serif; color: var(--text); }

  .logo-panel { position: absolute; left: 0; top: 0; width: 994px; height: 370px; background: var(--paper); }
  .stage { position: absolute; left: 0; top: 370px; width: 994px; height: 830px; background: var(--stage); }

  .wordmark { position: absolute; display: flex; align-items: center; }
  .wordmark .dot { border-radius: 50%; flex: none; }
  .wordmark .name { font-family: "Cinzel", serif; font-weight: 600; line-height: 1; white-space: nowrap; }
  .wordmark .name span { display: block; }

  .wordmark--hero { left: 236px; top: 120px; }
  .wordmark--hero .dot { width: 120px; height: 120px; background: var(--brand-blue); margin-right: 28px; }
  .wordmark--hero .name { color: var(--brand-blue); }
  .wordmark--hero .line-main { font-size: 46px; letter-spacing: 1px; }
  .wordmark--hero .line-sub { font-size: 22px; letter-spacing: 1px; margin-top: 10px; }

  .card { position: absolute; left: 219px; width: 552px; height: 330px; overflow: hidden; }
  .card--front { top: 431px; background: var(--paper); }
  .card--back { top: 811px; background: linear-gradient(135deg, var(--charcoal-light) 0%, var(--charcoal) 70%); }

  .card--front .wordmark { left: 250px; top: 30px; }
  .card--front .dot { width: 58px; height: 58px; background: var(--brand-blue); margin-right: 14px; }
  .card--front .name { color: var(--brand-blue); }
  .card--front .line-main { font-size: 21px; }
  .card--front .line-sub { font-size: 10.5px; margin-top: 5px; }

  .holder { position: absolute; left: 28px; top: 168px; }
  .holder-name { font-family: "Cinzel", serif; font-weight: 600; font-size: 18px; color: var(--brand-blue); }
  .holder-role { font-size: 13px; margin-top: 1px; }
  .divider { position: absolute; left: 28px; top: 222px; width: 374px; height: 1px; background: var(--rule); }
  .address { position: absolute; left: 28px; top: 244px; font-size: 13.5px; line-height: 17px; }

  .contacts { position: absolute; right: 26px; top: 213px; list-style: none; font-size: 13.5px; line-height: 20.5px; text-align: right; }
  .contacts li { display: flex; justify-content: flex-end; align-items: center; gap: 6px; }
  .contacts svg { width: 12px; height: 12px; fill: var(--brand-blue); }

  .card-band { position: absolute; left: 0; bottom: 0; }

  .card--back .wordmark { left: 296px; top: 222px; }
  .card--back .dot { width: 56px; height: 56px; background: var(--paper); margin-right: 12px; }
  .card--back .name { color: var(--paper); }
  .card--back .line-main { font-size: 21px; }
  .card--back .line-sub { font-size: 10px; margin-top: 5px; }
</style>
</head>
<body>
  <section class="logo-panel">
    <div class="wordmark wordmark--hero">
      <div class="dot"></div>
      <div class="name"><span class="line-main">TanRidge</span><span class="line-sub">Field Advisory Ltd</span></div>
    </div>
  </section>

  <section class="stage">
  </section>

  <article class="card card--front">
    <div class="wordmark">
      <div class="dot"></div>
      <div class="name"><span class="line-main">TanRidge</span><span class="line-sub">Field Advisory Ltd</span></div>
    </div>

    <div class="holder">
      <p class="holder-name">DANIEL MORROW</p>
      <p class="holder-role">Managing Director</p>
    </div>
    <div class="divider"></div>
    <p class="address">Suite 4, 102 Range Road<br>Sexsmith, Alberta</p>

    <ul class="contacts">
      <li>+ 000 000 0000 <svg viewBox="0 0 12 12"><rect x="3" y="0" width="6" height="12" rx="1"/></svg></li>
      <li>+ 000 000 0000 <svg viewBox="0 0 12 12"><path d="M0 5 Q6 0 12 5 L10 6 L9 4 Q6 3 3 4 L2 6 Z M2 7 H10 V11 H2 Z"/></svg></li>
      <li>info@tanridgefa.com <svg viewBox="0 0 12 12"><path d="M0 2 H12 V10 H0 Z" /></svg></li>
      <li>www.tanridgefa.com <svg viewBox="0 0 12 12"><circle cx="6" cy="6" r="5.5"/></svg></li>
    </ul>

    <svg class="card-band" width="552" height="26" viewBox="0 0 552 26">
      <defs>
        <linearGradient id="band-blue" x1="0" x2="1">
          <stop offset="0" stop-color="#1d2f7a"/>
          <stop offset="1" stop-color="#1c5a9e"/>
        </linearGradient>
      </defs>
      <polygon points="0,12 278,12 266,26 0,26" fill="url(#band-blue)"/>
      <polygon points="290,2 552,2 552,26 268,26" fill="#4a4a4a"/>
    </svg>
  </article>

  <article class="card card--back">
    <div class="wordmark">
      <div class="dot"></div>
      <div class="name"><span class="line-main">TanRidge</span><span class="line-sub">Field Advisory Ltd</span></div>
    </div>
  </article>
</body>
</html>
```